K&R Security Services PTY. LTD.

Ive just had my logo made and I'm looking for some simple but strong designs for my business cards the company is a security company.

Please use dark colors.

Regards,

Owen Deloit

Reason: Need more time for discussion with other directors

Industry/Entity Type

Security

Font styles to use
Sans Serif
Decorative

```html
<!DOCTYPE html>
<html lang="en">
<head>
<meta charset="utf-8">
<title>K&amp;R Security Services – Business Card</title>
<link rel="stylesheet" href="https://fonts.googleapis.com/css2?family=Cormorant+Garamond:wght@400;500&display=swap">
<style>
  :root {
    --backdrop: #1c1c1e;
    --card: #050505;
    --card-glow: #2a2a2a;
    --ink: #b9b9b9;
    --ink-soft: #8e8e8e;
    --rule: #6f6f6f;
    --ornament: #7a7a7a;
  }
  html, body {
    margin: 0;
    width: 1200px;
    height: 1000px;
    overflow: hidden;
    background: var(--backdrop);
  }
  .stage {
    position: relative;
    width: 1200px;
    height: 1000px;
  }
  .card {
    position: absolute;
    top: 345px;
    width: 540px;
    height: 310px;
    border-radius: 8px;
    background: var(--card);
    box-shadow: 0 12px 30px rgba(0,0,0,.6);
    overflow: hidden;
    font-family: "Cormorant Garamond", serif;
  }
  .card--back { left: 40px; }
  .card--front {
    left: 620px;
    background: radial-gradient(circle at 50% 50%, var(--card-glow) 0%, #111 45%, var(--card) 80%);
  }
  .frame {
    position: absolute;
    inset: 0;
  }
  .contact {
    position: absolute;
    left: 36px;
    top: 112px;
    color: var(--ink);
  }
  .contact__name {
    margin: 0 0 6px;
    font-size: 24px;
    font-weight: 500;
    letter-spacing: .3px;
  }
  .contact__line {
    margin: 0;
    font-size: 16px;
    line-height: 1.35;
    color: var(--ink-soft);
  }
  .brand {
    position: absolute;
    display: flex;
    align-items: center;
    gap: 8px;
    color: var(--ink);
    font-family: "Cormorant Garamond", serif;
    font-weight: 500;
    white-space: nowrap;
  }
  .brand__dot {
    border: 1.5px solid var(--ink);
    border-radius: 50%;
  }
  .brand--small {
    right: 44px;
    bottom: 62px;
    font-size: 17px;
  }
  .brand--small .brand__dot { width: 14px; height: 14px; }
  .brand--large {
    left: 50%;
    top: 50%;
    transform: translate(-50%, -50%);
    font-size: 30px;
  }
  .brand--large .brand__dot { width: 22px; height: 22px; }
</style>
</head>
<body>
<main class="stage">

  <section class="card card--back">
    <svg class="frame" width="540" height="310" viewBox="0 0 540 310">
      <rect role="img" aria-label="Small scroll ornament at top-left corner" x="14" y="10" width="30" height="12" rx="4" fill="var(--ornament)" opacity=".7"/>
      <line x1="48" y1="16" x2="300" y2="16" stroke="var(--rule)" stroke-width="1"/>
      <line x1="20" y1="26" x2="20" y2="260" stroke="var(--rule)" stroke-width="1"/>
      <rect role="img" aria-label="Small scroll ornament at bottom-right corner" x="496" y="288" width="30" height="12" rx="4" fill="var(--ornament)" opacity=".7"/>
      <line x1="240" y1="294" x2="492" y2="294" stroke="var(--rule)" stroke-width="1"/>
      <line x1="520" y1="50" x2="520" y2="284" stroke="var(--rule)" stroke-width="1"/>
    </svg>
    <div class="contact">
      <p class="contact__name">Owen Deloit</p>
      <p class="contact__line">0198 765 432</p>
      <p class="contact__line">owendeloit@krmail.net</p>
    </div>
    <div class="brand brand--small">
      <span class="brand__dot"></span>
      <span class="brand__name">K&amp;R Security Services</span>
    </div>
  </section>

  <section class="card card--front">
    <div class="brand brand--large">
      <span class="brand__dot"></span>
      <span class="brand__name">K&amp;R Security Services</span>
    </div>
  </section>

</main>
</body>
</html>
```